Old Fashioned, Artisan Goat Milk Soap Label

We are branching out in our goat milk dairy into artisan goat milk soaps. High quality, yet an old fashioned feel. Simple yet elegant. Emphasis on the milk and its moisturizing, healing, softening, and superiority.
Purity in a simple design that harkens back to a quaint, earlier time where quality ingredients were valued as much as quality workmanship.
Perhaps a drop symbolizing the milk, or a bucket pouring into or out of the logo. We already have our farm logo, Willowbrook Hollow, and were thinking the soap would be "Sweet Nell"
The labels will grace our liquid soap bottles and our bar soaps. 3.5" X 2.5"
The label color will be an antiqued ivory or other shade to convey a simpler time.

Reason: Realized that the contest length was short enough to scare away designers. Adding time to give entered designers time to create.

Target Market(s)

Upscale people looking to know where their products come from. People looking for better options, artisan products.

Requirements
Must have
• My project must have emphasis on the milk, old time feel, simple elegance
Nice to have
• Perhaps a drop symbolizing the milk, or a bucket pouring into or out of the logo. We already have our farm logo, Willowbrook Hollow, and were thinking the soap would be "Sweet Nell"
• If you use a goat, please be aware that we have the breed Nubians that have long luxurious ears and don't have horns.

```html
<!DOCTYPE html>
<html lang="en">
<head>
<meta charset="utf-8">
<title>Sweet Nell Goat Milk Soap – Label Options</title>
<link rel="stylesheet" href="https://fonts.googleapis.com/css2?family=Berkshire+Swash&family=Kalam:wght@400;700&family=Sorts+Mill+Goudy&display=swap">
<style>
  :root {
    --page: #ffffff;
    --frame-grey: #8c8c8c;
    --ivory: #f4eea9;
    --ivory-light: #f5efa6;
    --walnut: #4a2a0c;
    --cocoa: #3b2410;
    --caramel: #a9783a;
    --milk-brown: #9a6634;
    --ink: #2a1a0c;
    --aqua: #33e6f2;
    --bubble-line: #b9b39a;
    --ornament: #b88a4c;
  }
  * { box-sizing: border-box; margin: 0; padding: 0; }
  html, body { width: 1200px; height: 619px; overflow: hidden; background: var(--page); }
  .stage {
    position: relative; width: 1200px; height: 619px;
    border: 1.5px solid var(--frame-grey); background: var(--page);
  }
  .label { position: absolute; top: 104px; width: 278px; height: 384px; }
  .label svg.bubbles { position: absolute; inset: 0; width: 100%; height: 100%; }
  .art { position: absolute; border-radius: 40% 45% 40% 50%; }
  .art--goat { background: radial-gradient(ellipse at 50% 50%, #6b5a44 0%, #a8987a 55%, rgba(244,238,169,0) 75%); }
  .art--bucket { background: radial-gradient(ellipse at 50% 50%, #5a4632 0%, #9c8a6e 55%, rgba(244,238,169,0) 75%); }
  .script-line { font-family: "Kalam", cursive; font-weight: 700; text-align: center; position: absolute; left: 0; right: 0; }

  /* Option one */
  .label--ornate { left: 100px; background: var(--page); border: 1px solid var(--frame-grey); padding: 7px; }
  .label--ornate .field { position: relative; width: 100%; height: 100%; background: var(--ivory); }
  .corner { position: absolute; width: 36px; height: 36px; background: var(--ornament); opacity: .55; border-radius: 2px 50% 50% 50%; }
  .corner--tl { top: 4px; left: 4px; }
  .corner--tr { top: 4px; right: 4px; border-radius: 50% 2px 50% 50%; }
  .corner--bl { bottom: 4px; left: 4px; border-radius: 50% 50% 50% 2px; }
  .corner--br { bottom: 4px; right: 4px; border-radius: 50% 50% 2px 50%; }
  .stack-title { top: 26px; color: var(--milk-brown); font-size: 36px; line-height: 34px; }
  .name-plate {
    position: absolute; left: 29px; top: 173px; width: 216px; height: 56px;
    background: var(--walnut); color: var(--ivory);
    font-family: "Berkshire Swash", serif; font-size: 33px;
    display: flex; align-items: center; justify-content: center;
  }

  /* Option two */
  .label--framed { left: 434px; background: var(--page); border: 1px solid var(--frame-grey); padding: 3px; }
  .label--framed .field { position: relative; width: 100%; height: 100%; background: var(--ivory); border: 3px solid var(--cocoa); }
  .serif-name { font-family: "Sorts Mill Goudy", serif; color: var(--ink); position: absolute; left: 0; right: 0; text-align: center; }
  .label--framed .serif-name { top: 92px; font-size: 37px; font-weight: 700; -webkit-text-stroke: .6px var(--ink); }
  .label--framed .script-line { top: 280px; color: var(--aqua); font-size: 33px; font-weight: 400; }

  /* Option three */
  .label--bordered { left: 789px; background: var(--caramel); border: 1px solid var(--cocoa); padding: 14px; }
  .label--bordered .field { position: relative; width: 100%; height: 100%; background: var(--ivory-light); border: 1px solid var(--cocoa); }
  .label--bordered .serif-name { font-size: 72px; line-height: 1; }
  .serif-name--first { top: 38px; }
  .serif-name--second { top: 180px; }
  .label--bordered .script-line { top: 282px; color: var(--milk-brown); font-size: 27px; }
</style>
</head>
<body>
<main class="stage">

  <section class="label label--ornate">
    <div class="field">
      <span class="corner corner--tl"></span><span class="corner corner--tr"></span>
      <span class="corner corner--bl"></span><span class="corner corner--br"></span>
      <svg class="bubbles" viewBox="0 0 264 370" aria-hidden="true">
        <g fill="#fff" stroke="var(--bubble-line)" stroke-width="1">
          <circle cx="38" cy="52" r="4"/><circle cx="50" cy="90" r="7"/><circle cx="40" cy="112" r="5"/>
          <circle cx="52" cy="132" r="4"/><circle cx="34" cy="148" r="3"/><circle cx="196" cy="42" r="4"/>
          <circle cx="212" cy="56" r="6"/><circle cx="224" cy="74" r="4"/><circle cx="205" cy="96" r="5"/>
          <circle cx="222" cy="124" r="3"/><circle cx="198" cy="268" r="5"/><circle cx="215" cy="283" r="4"/>
          <circle cx="205" cy="300" r="6"/><circle cx="55" cy="300" r="4"/><circle cx="70" cy="312" r="3"/>
        </g>
      </svg>
      <p class="script-line stack-title">Goat<br>milk<br>soap</p>
      <div class="name-plate">Sweet Nell</div>
      <div class="art art--goat" role="img" aria-label="Ink drawing of a Nubian goat head" style="left:85px;top:262px;width:130px;height:78px;"></div>
    </div>
  </section>

  <section class="label label--framed">
    <div class="field">
      <svg class="bubbles" viewBox="0 0 264 372" aria-hidden="true">
        <g fill="#fff" stroke="var(--bubble-line)" stroke-width="1">
          <circle cx="70" cy="55" r="4"/><circle cx="88" cy="45" r="3"/><circle cx="80" cy="68" r="3"/>
          <circle cx="32" cy="160" r="5"/><circle cx="44" cy="178" r="4"/><circle cx="60" cy="170" r="6"/>
          <circle cx="210" cy="158" r="4"/><circle cx="222" cy="176" r="5"/><circle cx="205" cy="192" r="3"/>
          <circle cx="196" cy="232" r="4"/><circle cx="214" cy="244" r="6"/><circle cx="186" cy="256" r="4"/>
          <circle cx="206" cy="268" r="3"/>
        </g>
      </svg>
      <div class="art art--bucket" role="img" aria-label="Sketch of a wooden bucket pouring milk" style="left:163px;top:16px;width:68px;height:75px;"></div>
      <h2 class="serif-name">Sweet Nell</h2>
      <div class="art art--goat" role="img" aria-label="Ink drawing of a Nubian goat head" style="left:76px;top:168px;width:104px;height:84px;"></div>
      <p class="script-line">Goat milk soap</p>
    </div>
  </section>

  <section class="label label--bordered">
    <div class="field">
      <h2 class="serif-name serif-name--first">Sweet</h2>
      <div class="art art--bucket" role="img" aria-label="Sketch of a wooden bucket pouring milk" style="left:96px;top:145px;width:60px;height:52px;"></div>
      <h2 class="serif-name serif-name--second">Nell</h2>
      <p class="script-line">Goat milk soap</p>
    </div>
  </section>

</main>
</body>
</html>
```